" A vanta soluções de conexão é uma empresa de serviços que presta suporte e gerenciamento técnico para provedores de internet e outras empresas. "

```html
<!DOCTYPE html>
<html lang="pt-BR">
<head>
<meta charset="utf-8">
<title>Cartão de visita — vanta soluções de conexão</title>
<link href="https://fonts.googleapis.com/css2?family=Montserrat:wght@400;500;600;700&display=swap" rel="stylesheet">
<style>
  :root {
    --navy: #101a5e;
    --navy-deep: #0b1450;
    --cyan: #2fc6d8;
    --cyan-soft: #7fe0ea;
    --paper: #ffffff;
    --ink: #1b2360;
    --backdrop: #dcdde0;
  }
  * { margin: 0; padding: 0; box-sizing: border-box; }
  html, body { width: 1200px; height: 1200px; overflow: hidden; }
  body {
    background: var(--backdrop);
    font-family: "Montserrat", sans-serif;
    position: relative;
  }
  .card {
    position: absolute;
    left: 211px;
    width: 778px;
    height: 452px;
    border-radius: 22px;
    overflow: hidden;
  }
  .card-front { top: 154px; background: var(--navy); }
  .card-back { top: 644px; background: var(--paper); }

  .edge-tab {
    position: absolute;
    width: 22px;
    background: var(--cyan);
    border-radius: 10px;
  }
  .card-front .edge-tab { top: 62px; height: 262px; }
  .card-front .edge-left { left: -10px; }
  .card-front .edge-right { right: -10px; }
  .card-back .edge-left { left: -10px; top: 0; height: 452px; border-radius: 0; }
  .card-back .edge-right { right: -10px; top: 180px; height: 250px; }

  .brand {
    position: absolute;
    display: flex;
    align-items: center;
  }
  .brand-mark { background: var(--cyan); flex: none; }
  .brand-name { font-weight: 700; letter-spacing: 0.01em; white-space: nowrap; }

  .card-front .brand { left: 0; right: 0; top: 198px; justify-content: center; gap: 20px; }
  .card-front .brand-mark { width: 46px; height: 46px; }
  .card-front .brand-name { color: var(--paper); font-size: 40px; }

  .card-back .brand { left: 88px; top: 152px; gap: 14px; }
  .card-back .brand-mark { width: 28px; height: 28px; }
  .card-back .brand-name { color: var(--ink); font-size: 21px; }

  .holder { position: absolute; left: 442px; top: 104px; }
  .holder-name { font-size: 26px; font-weight: 600; color: var(--ink); }
  .holder-role { margin-top: 6px; font-size: 14px; font-weight: 500; letter-spacing: 0.14em; color: var(--cyan); }

  .contact-list { position: absolute; list-style: none; font-size: 17px; font-weight: 500; color: var(--ink); line-height: 1.3; }
  .contact-list li { display: flex; align-items: center; gap: 10px; margin-bottom: 6px; }
  .contact-left { left: 132px; top: 286px; }
  .contact-right { left: 436px; top: 290px; }
  .icon { width: 26px; height: 26px; flex: none; }
  .dot { width: 22px; height: 22px; border-radius: 50%; background: var(--cyan); flex: none; }
  .spacer { width: 26px; flex: none; }
</style>
</head>
<body>
  <section class="card card-front" aria-label="Frente do cartão">
    <span class="edge-tab edge-left"></span>
    <span class="edge-tab edge-right"></span>
    <div class="brand">
      <span class="brand-mark"></span>
      <span class="brand-name">vanta soluções de conexão</span>
    </div>
  </section>

  <section class="card card-back" aria-label="Verso do cartão">
    <span class="edge-tab edge-left"></span>
    <span class="edge-tab edge-right"></span>
    <div class="brand">
      <span class="brand-mark"></span>
      <span class="brand-name">vanta soluções de conexão</span>
    </div>

    <div class="holder">
      <p class="holder-name">Nome e Sobrenome</p>
      <p class="holder-role">DIRETOR COMERCIAL</p>
    </div>

    <ul class="contact-list contact-left">
      <li>
        <svg class="icon" viewBox="0 0 24 24" aria-hidden="true"><circle cx="12" cy="12" r="12" fill="#2fc6d8"/><path d="M8.6 6.5l1.8-.4 1.1 2.6-1.3 1c.6 1.3 1.6 2.3 2.9 2.9l1-1.3 2.6 1.1-.4 1.8c-.2.6-.7 1-1.3 1-4.1-.2-7.4-3.5-7.6-7.6 0-.6.4-1.1 1.2-1.1z" fill="#fff"/></svg>
        <span>(91) 3400-1200<br>(91) 98100-2345</span>
      </li>
      <li>
        <svg class="icon" viewBox="0 0 24 24" aria-hidden="true"><circle cx="12" cy="12" r="12" fill="#2fc6d8"/><path d="M12 5a4.5 4.5 0 0 0-4.5 4.5c0 3.4 4.5 9 4.5 9s4.5-5.6 4.5-9A4.5 4.5 0 0 0 12 5zm0 6.3a1.8 1.8 0 1 1 0-3.6 1.8 1.8 0 0 1 0 3.6z" fill="#fff"/></svg>
        <span>Rua das Antenas, 450 | Centro<br>CEP: 66010-200 | Cidade/UF</span>
      </li>
    </ul>

    <ul class="contact-list contact-right">
      <li>
        <svg class="icon" viewBox="0 0 24 24" aria-hidden="true"><circle cx="12" cy="12" r="12" fill="#2fc6d8"/><path d="M6.5 8.5h11v7h-11z" fill="none" stroke="#fff" stroke-width="1.5"/><path d="M6.5 8.5l5.5 4 5.5-4" fill="none" stroke="#fff" stroke-width="1.5"/></svg>
        <span>contato@vantaconexao.com<br>www.vantaconexao.com.br</span>
      </li>
      <li>
        <span class="dot"></span>
        <span>vanta.conexao</span>
      </li>
    </ul>
  </section>
</body>
</html>
```